Orvel Prime - Letter Head

My company is a residential and commercial cleaning company , which is located in Abu Dhabi, UAE.
I am looking for a creative letterhead reflects the professional and reflects professionalism and send the feeling of relax and comfort.
The color which will be used it has to be selected carefully in prospective of colors psychological effects, so every color to be used should be for a reason.
Also, reflecting my company colors in an attractive way.
Regarding the information which it should contains, it has to show the address, contacts , telephones an, email address and website.
Also, my company logo is attached
Residential

```html
<!DOCTYPE html>
<html lang="en">
<head>
<meta charset="utf-8">
<title>Orvel Prime - Letterhead</title>
<link href="https://fonts.googleapis.com/css2?family=Open+Sans:wght@400;700&display=swap" rel="stylesheet">
<style>
  :root {
    --canvas: #ffffff;
    --brand-blue: #0b55a8;
    --mark-faint: #eaf4fa;
    --sun-yellow: #fdbf16;
    --sun-shadow: #f2a64a;
    --grass: #acd033;
    --grass-light: #c8e85a;
    --lane: #ffffff;
    --ink-muted: #9a9a9a;
    --name-blue: #1b6fb8;
  }
  html, body {
    margin: 0;
    padding: 0;
    width: 1200px;
    height: 900px;
    overflow: hidden;
    background: var(--canvas);
    font-family: "Open Sans", Arial, sans-serif;
  }
  .sheet {
    position: absolute;
    left: 282px;
    top: 0;
    width: 636px;
    height: 900px;
    background: var(--canvas);
    overflow: hidden;
  }
  .top-band {
    position: absolute;
    left: 0; top: 0;
    width: 636px; height: 28px;
    background: linear-gradient(180deg, var(--brand-blue), #0a4f9c);
  }
  .faint-mark {
    position: absolute;
    left: 70px; top: 132px;
    width: 262px; height: 262px;
  }
  .sun-badge {
    position: absolute;
    left: 42px; top: 653px;
    width: 210px; height: 212px;
  }
  .brand-name {
    position: absolute;
    left: 58px; top: 730px;
    width: 190px;
    text-align: center;
    font-weight: 700;
    font-size: 26px;
    color: var(--name-blue);
    line-height: 1;
    white-space: nowrap;
  }
  .contact {
    position: absolute;
    top: 793px;
    font-size: 8.6px;
    line-height: 11px;
    color: var(--ink-muted);
    white-space: nowrap;
  }
  .contact--address { left: 270px; }
  .contact--phone { left: 476px; }
  .road {
    position: absolute;
    left: 0; top: 825px;
    width: 636px; height: 75px;
  }
</style>
</head>
<body>
  <div class="sheet">
    <div class="top-band" role="img" aria-label="Blue header band with a white zigzag rooftop pattern"></div>

    <svg class="faint-mark" viewBox="0 0 262 262" aria-hidden="true">
      <circle cx="131" cy="131" r="124" fill="none" stroke="var(--mark-faint)" stroke-width="10"/>
    </svg>

    <svg class="sun-badge" viewBox="0 0 210 212" aria-hidden="true">
      <circle cx="101" cy="109" r="102" fill="var(--sun-shadow)"/>
      <circle cx="106" cy="104" r="102" fill="var(--sun-yellow)"/>
    </svg>
    <div class="brand-name">Orvel Prime</div>

    <div class="contact contact--address">
      Unit 18, Lane 4, Sector 9, Harbor East 2,<br>
      Saltmere Business Park, United Arab Emirates
    </div>
    <div class="contact contact--phone">
      +971 2 555 0142, +971 2 555 0187<br>
      hello@orvelprime.ae
    </div>

    <svg class="road" viewBox="0 0 636 75" aria-hidden="true">
      <rect x="0" y="0" width="636" height="75" fill="var(--grass)"/>
      <rect x="0" y="0" width="636" height="5" fill="var(--grass-light)"/>
      <g fill="var(--lane)">
        <rect x="0" y="39" width="28" height="3"/>
        <rect x="68" y="39" width="28" height="3"/>
        <rect x="136" y="39" width="28" height="3"/>
        <rect x="204" y="39" width="28" height="3"/>
        <rect x="272" y="39" width="28" height="3"/>
        <rect x="340" y="39" width="28" height="3"/>
        <rect x="408" y="39" width="28" height="3"/>
        <rect x="476" y="39" width="28" height="3"/>
        <rect x="544" y="39" width="28" height="3"/>
        <rect x="612" y="39" width="28" height="3"/>
      </g>
    </svg>
  </div>
</body>
</html>
```